Tech and Gadget Blog - News Site

I'm looking for someone to help design a wordpress theme for a tech news site that I'm creating.

I'll need the elements to be from right to left please because it's going to be in Arabic.

There are three main elements to the site.
1) We'll be publishing news on a daily basis (blog style) - Corvixel style

2) We'll have a section dedicated to the different programs we produce on vidmorra (so people should be able to view our latest content but also be able to filter based on the program.

3) We want it to be easy for people to comment and share (so having a good sharebar (like spreadnomic) and using disqus will be important too.

Of course it's important for us to have positions for banners so that we can monetize the site too and that the site is responsive.

You can see our channel here https://www.vidmorra.example/channel/UC8kqpwzrLMAXTNoa3h-r_Pq

One other very important page is a page for people to submit interest for advertising and advertorials. So that page will need to look very professional.

Target Market(s)

tech focused

Industry/Entity Type

Media

Coding

Coded - Design and coding required

Number of Pages Required

5+ page

Font styles to use
Sans Serif

Colors
09ab93
f59195
ffffff

Requirements
Must have
• using Wordpress as the CMS

```html
<!DOCTYPE html>
<html lang="en">
<head>
<meta charset="utf-8">
<title>Bitsora — Tech and Gadget News</title>
<link href="https://fonts.googleapis.com/css2?family=Open+Sans:wght@400;600;700&family=Roboto:wght@300;400;500&display=swap" rel="stylesheet">
<style>
:root{
  --teal:#09ab93;
  --teal-dark:#07937e;
  --teal-light:#3cc0ab;
  --pink:#f59195;
  --salmon:#ec6b68;
  --ink:#222;
  --text:#444;
  --muted:#888;
  --line:#e2e2e2;
  --soft:#f4f4f4;
  --foot:#3c3c3c;
  --foot-dark:#2d2d2d;
  --white:#fff;
}
*{box-sizing:border-box;margin:0;padding:0}
html,body{width:1200px;height:2985px;overflow:hidden;background:var(--white);font-family:"Open Sans",sans-serif;color:var(--text)}
.page{position:relative;width:1200px;height:2985px}
.abs{position:absolute}
.top-rule{left:0;top:0;width:1200px;height:4px;background:var(--teal)}

/* header */
.brand{left:80px;top:22px;display:flex;align-items:center;gap:12px}
.brand-mark{width:44px;height:44px;border-radius:8px;background:var(--teal)}
.brand-name{font-family:"Roboto",sans-serif;font-size:30px;font-weight:500;color:var(--teal)}
.lang{left:846px;top:42px;width:100px;height:32px;border:1px solid var(--line);display:flex;align-items:center;gap:8px;padding:0 8px;font-size:12px;color:#555}
.lang .flag{width:20px;height:13px;background:#2b4a8c;flex:none}
.lang svg{margin-left:auto}
.socials{display:flex;gap:6px}
.socials span{width:34px;height:34px;border-radius:50%;display:block}
.s1{background:#3b5a9a}.s2{background:#35b2e8}.s3{background:#1279b5}.s4{background:#f2a02a}
.head-social{left:956px;top:40px}
.call{left:596px;top:88px;display:flex;align-items:center;gap:10px}
.call-icon{width:38px;height:38px;border:2px solid var(--teal);border-radius:50%;display:flex;align-items:center;justify-content:center}
.call-label{font-size:13px;color:#555;line-height:16px}
.call-num{font-size:17px;font-weight:600;color:var(--salmon)}
.search{left:792px;top:92px;width:310px;height:42px;border:1px solid #d5d5d5;display:flex}
.search input{flex:1;min-width:0;border:0;padding:0 12px;font:13px "Open Sans",sans-serif;color:#999;outline:0}
.search button{width:44px;border:0;background:var(--teal);display:flex;align-items:center;justify-content:center}

/* nav */
.nav{left:0;top:176px;width:1200px;height:54px;background:linear-gradient(var(--teal-light),var(--teal))}
.nav ul{list-style:none;display:flex;position:absolute;left:100px;top:0;height:54px}
.nav li{height:54px;display:flex;align-items:center;justify-content:center;font-size:12px;font-weight:600;color:var(--white);border-right:1px solid rgba(255,255,255,.25)}
.nav li.active{background:var(--pink)}

/* hero */
.hero{left:0;top:230px;width:1200px;height:516px;background:linear-gradient(120deg,#b9b2a6 0%,#d8d0c6 40%,#c9b9a8 65%,#9d958d 100%)}
.hero-text{left:646px;top:600px;color:var(--white);font-family:"Roboto",sans-serif}
.hero-text h2{font-size:42px;font-weight:400;letter-spacing:.5px}
.hero-text p{font-size:28px;font-weight:300;margin-left:8px;margin-top:-2px}
.arrow-l{left:30px;top:468px}.arrow-r{left:1140px;top:468px}

/* common */
.box{border:1px solid var(--line);box-shadow:0 0 4px rgba(0,0,0,.06);background:var(--white)}
.sec-title{font-family:"Roboto",sans-serif;font-size:28px;font-weight:400;color:var(--salmon)}
.ph{display:block;flex:none}
.meta{font-size:11px;color:var(--muted);display:flex;gap:12px;align-items:center;white-space:nowrap}
.body-s{font-size:12.5px;line-height:22px;color:#333}
.more{font-size:13px;color:var(--salmon)}

/* daily */
.daily{left:100px;top:786px;width:676px;height:498px}
.daily .sec-title{position:absolute;left:18px;top:14px}
.feature{position:absolute;left:18px;top:62px;width:308px}
.feature .ph{width:308px;height:206px;background:linear-gradient(#7fd3d0,#52b5b8)}
.feature h3{font-family:"Roboto",sans-serif;font-size:23px;font-weight:400;color:var(--ink);line-height:30px;margin-top:14px}
.feature .meta{margin-top:8px}
.feature .body-s{margin-top:2px}
.mini-list{position:absolute;left:358px;top:62px;width:300px}
.mini{display:flex;gap:10px;height:105px}
.mini .ph{width:88px;height:86px;background:linear-gradient(#9aa7b3,#6c7785);border:1px solid var(--line)}
.mini p{font-size:12px;line-height:21px;color:#333;width:196px}
.mini .meta{margin-top:2px}

/* latest news */
.news{left:100px;top:1306px;width:676px;height:884px}
.news .sec-title{position:absolute;left:18px;top:14px}
.news-item{position:absolute;left:18px;width:640px;display:flex;gap:16px}
.news-item .ph{width:276px;height:174px}
.news-item h3{font-family:"Roboto",sans-serif;font-size:20px;font-weight:400;color:var(--ink);margin-top:-4px}
.news-item .meta{margin:4px 0 2px}

/* right column */
.post-card{left:790px;width:316px;height:296px}
.post-card .ph{width:314px;height:172px}
.post-card .cat{font-size:13px;color:#333;margin:16px 0 0 16px}
.post-card h3{font-family:"Roboto",sans-serif;font-size:22px;font-weight:400;color:var(--ink);line-height:29px;margin:2px 16px 0}
.post-card .by{font-size:11px;color:#555;margin:6px 0 0 16px}
.widget-head{height:54px;background:linear-gradient(var(--teal-light),var(--teal));color:var(--white);font-family:"Roboto",sans-serif;font-size:21px;padding:14px 20px}
.latest{left:790px;top:1406px;width:316px;height:506px}
.lp{display:flex;gap:10px;padding:10px 10px;height:112px;border-bottom:1px solid var(--line)}
.lp:last-child{border-bottom:0}
.lp .ph{width:86px;height:86px;background:linear-gradient(#c7c0b5,#8e857a)}
.lp h4{font-family:"Roboto",sans-serif;font-size:16px;font-weight:400;color:var(--ink);white-space:nowrap}
.lp p{font-size:12px;line-height:20px;color:#333}
.newsletter{left:790px;top:1928px;width:316px;height:264px}
.newsletter .intro{font-size:12.5px;color:#333;margin:16px 0 0 20px}
.field{width:268px;height:42px;border:1px solid #d8d8d8;margin:20px 0 0 20px;font-size:12px;color:#888;padding:12px 14px}
.field+.field{margin-top:14px}
.btn{display:inline-block;background:linear-gradient(var(--teal-light),var(--teal));color:var(--white);font-size:13px;border-radius:2px;padding:11px 38px}
.newsletter .btn{margin:16px 0 0 20px}

/* publish band */
.band{left:0;top:2244px;width:1200px;height:466px;background:var(--soft)}
.band .sec-title{position:absolute;left:100px;top:38px}
.pub{position:absolute;top:100px;width:226px}
.pub .ph{width:226px;height:174px;border:4px solid var(--white);box-shadow:0 0 3px rgba(0,0,0,.15)}
.pub h3{font-family:"Roboto",sans-serif;font-size:19px;font-weight:400;color:var(--ink);margin-top:18px}
.pub .meta{margin:6px 0 2px}
.pub .more{color:var(--teal)}

/* footer */
.footer{left:0;top:2710px;width:1200px;height:240px;background:var(--foot);color:#ddd}
.fcol{position:absolute;top:32px}
.fcol h5{font-family:"Roboto",sans-serif;font-size:19px;font-weight:400;color:var(--white);margin-bottom:10px}
.fcol p{font-size:12.5px;line-height:22px;color:#ddd}
.fcol ul{list-style:none}
.fcol li{font-size:12px;line-height:21.5px;color:#ddd}
.fcol li::before{content:"›";margin-right:8px}
.foot-field{width:252px;height:40px;background:var(--white);font-size:11px;color:#888;padding:12px 10px;margin-top:14px}
.fcol .btn{margin-top:12px;padding:10px 40px}
.bottom{left:0;top:2950px;width:1200px;height:35px;background:var(--foot-dark);font-size:11px;color:#ccc}
.bottom .copy{position:absolute;left:100px;top:10px}
.bottom .socials{position:absolute;left:958px;top:2px}
.bottom .socials span{width:30px;height:30px}
</style>
</head>
<body>
<div class="page">
  <div class="abs top-rule"></div>

  <header>
    <div class="abs brand"><span class="brand-mark"></span><span class="brand-name">Bitsora</span></div>
    <div class="abs lang"><span class="flag"></span>English
      <svg width="10" height="6" viewBox="0 0 10 6"><path d="M1 1l4 4 4-4" stroke="#666" fill="none" stroke-width="1.5"/></svg></div>
    <div class="abs socials head-social"><span class="s1"></span><span class="s2"></span><span class="s3"></span><span class="s4"></span></div>
    <div class="abs call">
      <span class="call-icon"><svg width="18" height="18" viewBox="0 0 24 24"><path d="M6.6 10.8a15 15 0 006.6 6.6l2.2-2.2a1 1 0 011-.25 11.4 11.4 0 003.6.6 1 1 0 011 1V20a1 1 0 01-1 1A17 17 0 013 4a1 1 0 011-1h3.5a1 1 0 011 1c0 1.25.2 2.45.57 3.57a1 1 0 01-.25 1z" fill="#09ab93"/></svg></span>
      <div><div class="call-label">Call Us :</div><div class="call-num">( 1555 ) 018 442</div></div>
    </div>
    <div class="abs search"><input value="Enter your keywords...." readonly><button aria-label="Search"><svg width="16" height="16" viewBox="0 0 16 16"><circle cx="6.5" cy="6.5" r="5" stroke="#fff" stroke-width="2" fill="none"/><path d="M10.5 10.5l4 4" stroke="#fff" stroke-width="2"/></svg></button></div>
  </header>

  <nav class="abs nav"><ul>
    <li class="active" style="width:130px">HOME</li>
    <li style="width:180px">ENTERTAINMENT</li>
    <li style="width:140px">SCIENCE</li>
    <li style="width:120px">VIDEO</li>
    <li style="width:130px">REVIEWS</li>
    <li style="width:140px">PUBLIC ACCESS</li>
    <li style="width:160px;border-right:0">CONTACT</li>
  </ul></nav>

  <section class="abs hero" role="img" aria-label="Smiling woman holding a camera on a desk with a laptop, tablet and photos"></section>
  <svg class="abs arrow-l" width="20" height="36" viewBox="0 0 20 36"><path d="M16 2L4 18l12 16" stroke="#fff" stroke-width="2" fill="none" opacity=".8"/></svg>
  <svg class="abs arrow-r" width="20" height="36" viewBox="0 0 20 36"><path d="M4 2l12 16L4 34" stroke="#fff" stroke-width="2" fill="none" opacity=".8"/></svg>
  <div class="abs hero-text"><h2>TECH AND GADGET</h2><p>POPULAR POSTS</p></div>

  <section class="abs box daily">
    <h2 class="sec-title">Daily basis like corvixel</h2>
    <article class="feature">
      <div class="ph" role="img" aria-label="Video presenter in front of a teal lights backdrop"></div>
      <h3>If you wanted to get rich, how would you do it?</h3>
      <div class="meta"><span>◉ 224</span><span>◌ 01 Comments</span></div>
      <p class="body-s">Lorem Ipsum is simply dummy text of the printing and typesetting industry. Lorem Ipsum has been the industry's standard dummy text ever since the 1500s, when an unknown printer took a galley</p>
      <a class="more">Read more &gt;&gt;</a>
    </article>
    <div class="mini-list">
      <div class="mini"><div class="ph" role="img" aria-label="Presenter video thumbnail"></div><div><p>Startups usually involve technology, so much so that the...industry. Lorem Ipsum text</p><div class="meta"><span>▦ Nov 03 , 2015</span><span>◌ 4 comments</span></div></div></div>
      <div class="mini"><div class="ph" role="img" aria-label="Presenter video thumbnail"></div><div><p>Startups usually involve technology, so much so that the...industry. Lorem Ipsum text</p><div class="meta"><span>▦ Nov 03 , 2015</span><span>◌ 4 comments</span></div></div></div>
      <div class="mini"><div class="ph" role="img" aria-label="Presenter video thumbnail"></div><div><p>Startups usually involve technology, so much so that the...industry. Lorem Ipsum text</p><div class="meta"><span>▦ Nov 03 , 2015</span><span>◌ 4 comments</span></div></div></div>
      <div class="mini"><div class="ph" role="img" aria-label="Presenter video thumbnail"></div><div><p>Startups usually involve technology, so much so that the...industry. Lorem Ipsum text</p><div class="meta"><span>▦ Nov 03 , 2015</span><span>◌ 4 comments</span></div></div></div>
    </div>
  </section>

  <section class="abs box news">
    <h2 class="sec-title">Latest news</h2>
    <article class="news-item" style="top:68px"><div class="ph" role="img" aria-label="Hands holding a smartphone beside a laptop" style="background:linear-gradient(#7a95b0,#3d4d63)"></div><div><h3>Voluptatem accusantium dolor</h3><div class="meta"><span>▦ Nov 03 , 2015</span><span>◌ 4 comments</span><span>⇪ 10 share</span></div><p class="body-s">Lorem Ipsum is simply dummy text of the printing and typesetting industry. Lorem Ipsum has been the industry's standard dummy text.Lorem Ipsum is simply dummy text of the printing and typesetting industry. Lorem Ipsum is simply dummy text of the printing</p><a class="more">Read more &gt;&gt;</a></div></article>
    <article class="news-item" style="top:272px"><div class="ph" role="img" aria-label="Cyclist using a phone with a heart rate app" style="background:linear-gradient(#b7cf8f,#6c8a55)"></div><div><h3>Laudantium, totam rem</h3><div class="meta"><span>▦ Nov 03 , 2015</span><span>◌ 4 comments</span><span>⇪ 10 share</span></div><p class="body-s">Lorem Ipsum is simply dummy text of the printing and typesetting industry. Lorem Ipsum has been the industry's standard dummy text.Lorem Ipsum is simply dummy text of the printing and typesetting industry. Lorem Ipsum is simply dummy text of the printing</p><a class="more">Read more &gt;&gt;</a></div></article>
    <article class="news-item" style="top:478px"><div class="ph" role="img" aria-label="Smartphone, camera and earphones on a dark desk" style="background:linear-gradient(#5a5a5a,#262626)"></div><div><h3>Blanditiis praesentium</h3><div class="meta"><span>▦ Nov 03 , 2015</span><span>◌ 4 comments</span><span>⇪ 10 share</span></div><p class="body-s">Lorem Ipsum is simply dummy text of the printing and typesetting industry. Lorem Ipsum has been the industry's standard dummy text.Lorem Ipsum is simply dummy text of the printing and typesetting industry. Lorem Ipsum is simply dummy text of the printing</p><a class="more">Read more &gt;&gt;</a></div></article>
    <article class="news-item" style="top:684px"><div class="ph" role="img" aria-label="Laptop, notebook and gadgets on a wooden desk" style="background:linear-gradient(#b08a62,#6d5440)"></div><div><h3>Voluptatum deleniti atque</h3><div class="meta"><span>▦ Nov 03 , 2015</span><span>◌ 4 comments</span><span>⇪ 10 share</span></div><p class="body-s">Lorem Ipsum is simply dummy text of the printing and typesetting industry. Lorem Ipsum has been the industry's standard dummy text.Lorem Ipsum is simply dummy text of the printing and typesetting industry. Lorem Ipsum is simply dummy text of the printing</p><a class="more">Read more &gt;&gt;</a></div></article>
  </section>

  <article class="abs box post-card" style="top:786px">
    <div class="ph" role="img" aria-label="Phone with earphones and coffee on a wooden table" style="background:linear-gradient(#a08468,#5e4a38)"></div>
    <div class="cat">Mobile</div>
    <h3>If you wanted to get rich, how would you do it?</h3>
    <div class="by">By R. Tamsin,&nbsp;&nbsp; 02.26.16</div>
  </article>
  <article class="abs box post-card" style="top:1092px">
    <div class="ph" role="img" aria-label="Smartphone resting on a laptop keyboard" style="background:linear-gradient(#d9d4cc,#9e968b)"></div>
    <div class="cat">Mobile</div>
    <h3>If you wanted to get rich, how would you do it?</h3>
    <div class="by">By R. Tamsin,&nbsp;&nbsp; 02.26.16</div>
  </article>

  <aside class="abs box latest">
    <div class="widget-head">Latest Posts</div>
    <div class="lp"><div class="ph" role="img" aria-label="Fitness bands"></div><div><h4>Possimus, omnis volup</h4><div class="meta"><span>▦ Nov 03 , 2015</span><span>◌ 4 comments</span></div><p>Startups usually involve technology, so much today.</p></div></div>
    <div class="lp"><div class="ph" role="img" aria-label="Hand holding a phone"></div><div><h4>Odio dignissimos ducimus</h4><div class="meta"><span>▦ Nov 03 , 2015</span><span>◌ 4 comments</span></div><p>Startups usually involve technology, so much today.</p></div></div>
    <div class="lp"><div class="ph" role="img" aria-label="Tablet showing a sale screen"></div><div><h4>Voluptatum deleniti</h4><div class="meta"><span>▦ Nov 03 , 2015</span><span>◌ 4 comments</span></div><p>Startups usually involve technology, so much today.</p></div></div>
    <div class="lp"><div class="ph" role="img" aria-label="Hands on a tablet"></div><div><h4>Corrupti quos</h4><div class="meta"><span>▦ Nov 03 , 2015</span><span>◌ 4 comments</span></div><p>Startups usually involve technology, so much today.</p></div></div>
  </aside>

  <aside class="abs box newsletter">
    <div class="widget-head">Newsletter</div>
    <p class="intro">Get monthly fresh updates in your mailbox</p>
    <div class="field">Enter your name...</div>
    <div class="field">Email address...</div>
    <span class="btn">Submit</span>
  </aside>

  <section class="abs band">
    <h2 class="sec-title">Tech and gadget to publish</h2>
    <article class="pub" style="left:100px"><div class="ph" role="img" aria-label="Laptop and phone on a desk" style="background:linear-gradient(#8aa3c4,#445a7a)"></div><h3>Accusamus et iusto odio</h3><div class="meta"><span>▦ Nov 03 , 2015</span><span>◌ 4 comments</span></div><p class="body-s">Lorem Ipsum is simply dummy text of the printing and typesetting industry. Lorem Ipsum has been the industry's</p><a class="more">Read more &gt;&gt;</a></article>
    <article class="pub" style="left:358px"><div class="ph" role="img" aria-label="Hand on a mouse with charts behind" style="background:linear-gradient(#b9d2dc,#6d93a3)"></div><h3>Dignissimos ducimu</h3><div class="meta"><span>▦ Nov 03 , 2015</span><span>◌ 4 comments</span></div><p class="body-s">Lorem Ipsum is simply dummy text of the printing and typesetting industry. Lorem Ipsum has been the industry's</p><a class="more">Read more &gt;&gt;</a></article>
    <article class="pub" style="left:616px"><div class="ph" role="img" aria-label="Hands typing on a laptop with warm light" style="background:linear-gradient(#e3a765,#9b6a45)"></div><h3>Nam libero tempore</h3><div class="meta"><span>▦ Nov 03 , 2015</span><span>◌ 4 comments</span></div><p class="body-s">Lorem Ipsum is simply dummy text of the printing and typesetting industry. Lorem Ipsum has been the industry's</p><a class="more">Read more &gt;&gt;</a></article>
    <article class="pub" style="left:876px"><div class="ph" role="img" aria-label="White earphones beside a phone" style="background:linear-gradient(#e8e8e8,#a9a9a9)"></div><h3>Cum soluta nobis est</h3><div class="meta"><span>▦ Nov 03 , 2015</span><span>◌ 4 comments</span></div><p class="body-s">Lorem Ipsum is simply dummy text of the printing and typesetting industry. Lorem Ipsum has been the industry's</p><a class="more">Read more &gt;&gt;</a></article>
  </section>

  <footer class="abs footer">
    <div class="fcol" style="left:98px;width:230px"><h5>ABOUT US</h5><p>Lorem Ipsum is simply dummy text of the printing and typesetting industry. Lorem Ipsum has been the industry's standard dummy text ever since the 1500s, when an unknown printer took a galley of type and scrambled</p></div>
    <div class="fcol" style="left:384px"><h5>QUICK LINKS</h5><ul><li>Home</li><li>Entertainment</li><li>Science</li><li>Video</li><li>Reviews</li><li>Public Access</li><li>Contact</li></ul></div>
    <div class="fcol" style="left:632px"><h5>SUPPORT</h5><ul><li>Privacy Policy</li><li>Terms &amp; Conditions</li><li>Sitemap</li></ul></div>
    <div class="fcol" style="left:852px;width:256px"><h5>NEWSLETTER</h5><p>Sed ut perspiciatis unde omnis iste natus error sit voluptatem accusantium</p><div class="foot-field">Enter your email address.....</div><span class="btn">Submit</span></div>
  </footer>
  <div class="abs bottom"><span class="copy">Copyright 2016 . All Rights Reserved</span><div class="socials"><span class="s1"></span><span class="s2"></span><span class="s3"></span><span class="s4"></span></div></div>
</div>
</body>
</html>
```